Cosmetic Clinic Looking For Sign Designs

We are looking for sign design ideas for the front of our building and a lawn sign for our cosmetic injection salon.
I have uploaded the front of our building for a mock up and size, lawn posts with size and a sign that uses the same dimensions.
We would like both signs to be black for the background.

Target Market(s)

Ages 18-75

Industry/Entity Type

Beauty

Requirements
Must have
• Services we offer:
• Cosmetic Injections
• Airbrush Spray Tanning
• Eyelash Growth Serum
• Skin Care Products & More
• Everything must be on a black background
• The lawn sign must have the address: 483 Fenwick and the building sign should have the phone number.
Should not have
• Nothing can light up (no LED)
• Both signs do not need the full address. Just 483 Fenwick and the phone number

```html
<!DOCTYPE html>
<html lang="en">
<head>
<meta charset="utf-8">
<title>Luma Bloom Salon – Sign Designs</title>
<link rel="stylesheet" href="https://fonts.googleapis.com/css2?family=Roboto+Condensed:wght@300;400;700&family=Roboto:wght@300;400&family=EB+Garamond:wght@400;600&display=swap">
<style>
  :root {
    --page: #ffffff;
    --sign-black: #111111;
    --board-top: #2a2824;
    --board-bottom: #161512;
    --gold: #d1a640;
    --gold-light: #f3dc8c;
    --gold-deep: #a77a1e;
    --white: #ffffff;
    --cream: #f4efe4;
  }
  html, body {
    margin: 0;
    padding: 0;
    width: 1015px;
    height: 1200px;
    overflow: hidden;
    background: var(--page);
  }
  .canvas {
    position: relative;
    width: 1015px;
    height: 1200px;
  }
  .lawn-sign {
    position: absolute;
    left: 28px;
    top: 298px;
    width: 470px;
    height: 616px;
  }
  .building-sign {
    position: absolute;
    left: 512px;
    top: 352px;
    width: 496px;
    height: 496px;
  }
  .wordmark {
    font-family: "Roboto Condensed", "Arial Narrow", sans-serif;
    font-weight: 700;
  }
  .subtitle {
    font-family: "Roboto", Arial, sans-serif;
    font-weight: 300;
  }
  .services {
    font-family: "EB Garamond", Garamond, serif;
    font-weight: 400;
  }
  .address {
    font-family: "EB Garamond", Garamond, serif;
    font-weight: 600;
  }
  .phone {
    font-family: "Roboto Condensed", "Arial Narrow", sans-serif;
    font-weight: 300;
  }
</style>
</head>
<body>
<main class="canvas">

  <!-- Lawn sign -->
  <svg class="lawn-sign" viewBox="0 0 587 770" role="group" aria-label="Lawn sign for Luma Bloom Salon">
    <defs>
      <path id="sign-outline" d="M0,110 A55,55 0 0 0 55,55 L170,55 C230,55 250,0 293.5,0 C337,0 357,55 417,55 L532,55 A55,55 0 0 0 587,110 L587,660 A55,55 0 0 0 532,715 L417,715 C357,715 337,770 293.5,770 C250,770 230,715 170,715 L55,715 A55,55 0 0 0 0,660 Z"/>
      <linearGradient id="gold-frame" x1="0" y1="0" x2="1" y2="1">
        <stop offset="0" stop-color="var(--gold-deep)"/>
        <stop offset="0.35" stop-color="var(--gold-light)"/>
        <stop offset="0.65" stop-color="var(--gold)"/>
        <stop offset="1" stop-color="var(--gold-light)"/>
      </linearGradient>
      <linearGradient id="board-fill" x1="0" y1="0" x2="0" y2="1">
        <stop offset="0" stop-color="var(--board-top)"/>
        <stop offset="1" stop-color="var(--board-bottom)"/>
      </linearGradient>
      <radialGradient id="gold-disc" cx="0.4" cy="0.35" r="0.7">
        <stop offset="0" stop-color="var(--gold-light)"/>
        <stop offset="1" stop-color="var(--gold-deep)"/>
      </radialGradient>
    </defs>

    <use href="#sign-outline" fill="var(--sign-black)"/>
    <use href="#sign-outline" fill="url(#board-fill)" stroke="url(#gold-frame)" stroke-width="13"
         transform="translate(293.5 385) scale(0.915 0.935) translate(-293.5 -385)"/>

    <circle class="brand-disc" cx="293.5" cy="130" r="74" fill="url(#gold-disc)"/>

    <text class="wordmark" x="293.5" y="283" text-anchor="middle" font-size="74" fill="var(--gold)">LUMA BLOOM</text>
    <line x1="113" y1="320" x2="228" y2="320" stroke="var(--gold)" stroke-width="3"/>
    <line x1="359" y1="320" x2="474" y2="320" stroke="var(--gold)" stroke-width="3"/>
    <text class="subtitle" x="293.5" y="334" text-anchor="middle" font-size="40" fill="var(--gold)">SALON</text>

    <g class="services" text-anchor="middle" font-size="37" fill="var(--cream)">
      <text x="293.5" y="406">Cosmetic Injections</text>
      <text x="293.5" y="460">Airbrush Spray Tanning</text>
      <text x="293.5" y="514">Eyelash Growth Serum</text>
      <text x="293.5" y="568">Skin Care Products &amp; More</text>
    </g>

    <text class="address" x="293.5" y="690" text-anchor="middle" font-size="27" fill="var(--gold)">483 FENWICK</text>
  </svg>

  <!-- Building sign -->
  <svg class="building-sign" viewBox="0 0 640 640" role="group" aria-label="Round building sign for Luma Bloom Salon">
    <circle cx="320" cy="320" r="318" fill="var(--sign-black)"/>
    <circle cx="320" cy="320" r="298" fill="none" stroke="var(--white)" stroke-width="5"/>

    <circle class="brand-disc" cx="320" cy="136" r="100" fill="none" stroke="var(--white)" stroke-width="14"/>

    <text class="wordmark" x="320" y="352" text-anchor="middle" font-size="100" fill="var(--white)">LUMA BLOOM</text>
    <line x1="62" y1="393" x2="215" y2="393" stroke="var(--white)" stroke-width="4"/>
    <line x1="425" y1="393" x2="578" y2="393" stroke="var(--white)" stroke-width="4"/>
    <text class="subtitle" x="320" y="410" text-anchor="middle" font-size="52" fill="var(--white)">SALON</text>

    <text class="phone" x="320" y="517" text-anchor="middle" font-size="72" fill="var(--white)">(555)284-3190</text>
  </svg>

</main>
</body>
</html>
```